Advertisement for my roofing company

Looking to get designs for:

- Secondary Logo
- Business card designs
- Small Yard Signs (like the KVQ/Bolt Security signs people put at the mail box to let bad guys know there's camera's)
- Quick Door note/flyer to leave while canvassing letting them know we are working in neighborhoods/area and want to check out their roof to see if it qualifies for roof replacement paid for by insurance.
- any other good ideas not commoningly used that is different and stands out from everyone else

We are in need of some help getting a page designed for a high school football game program packet that the school will sell to locals with all the team information in it for this years team. We are planning to do a full page for our company branding, is this something you guys can help me with? They are requesting a PDF final copy by July 1st.

Just want to advertise what we do for homeowners after a storm impacts their areas.

Basically a quick summary about our company.

We are a roofing company that specialize in storm restoration and insurance claims. Prior to the start up of duo mark me and the business partner were insurance adjuster that handle property claims after major storm event all over the country and work storm like hurricanes to snow storms that caused damage so that gives the property owner the advantage when they use us after a storm because we have over 25+ years of insurance adjusting back ground and knowledge for the major carriers people use. We also provide other services like roof repairs, gutters systems, siding, painting interior/exterior, and windows. Main focus is roofing though! We do tons of door knocking to in area that are recently impacted by storms and offer free inspections to homeowner/property owners who are concerned or curious how their roof/property held up during the storm. We also offer inspections with a Drone Inspections using VELTRIX AI HAZARD SCANNING SYSTEM for those people who just feel more comfortable with that. ( which is huge and helps us land lots of leads )

We proudly carry the highest residential certification with all the large roofing material manufactures. We are WBN Sovereign Crown Select with WBN and Ridge Keeper w/ Faulbrook which are the only two we install anymore due to the fact the rest of them are trash.

Don't use all that or anything but this just gives you a idea what we represent.

Target Market(s)

Homeowners/property owners

Industry/Entity Type

Roofing

Font styles to use
Sans Serif

Colors
EB3D1F
EC4F4E
F09395
F8D3D4
FCEDEE

Requirements
Nice to have
• Modern design look
Should not have
• Generic google/online photos.

```html
<!DOCTYPE html>
<html lang="en">
<head>
<meta charset="utf-8">
<title>Duo Mark Roofing – Flyer</title>
<link href="https://fonts.googleapis.com/css2?family=Montserrat:wght@500;600;700;800&display=swap" rel="stylesheet">
<style>
  :root{
    --red:#b7191e;
    --charcoal:#3a3b40;
    --ink:#2e2f33;
    --sand:#ece9e3;
    --white:#ffffff;
    --photo-sky:#3a3b40;
    --photo-siding:#5d6878;
    --photo-roof:#8a7f74;
    --photo-stone:#4a433d;
    --photo-lawn:#5f8a3a;
    --map-green:#b6dcc0;
  }
  html,body{margin:0;padding:0;width:991px;height:1200px;overflow:hidden;background:var(--white);}
  .flyer{position:relative;width:991px;height:1200px;overflow:hidden;background:var(--white);font-family:"Montserrat",sans-serif;color:var(--ink);}
  .flyer-shapes{position:absolute;inset:0;}
  .contact-bar{position:absolute;top:16px;left:0;width:991px;height:26px;font-weight:600;font-size:17px;color:var(--charcoal);}
  .contact-item{position:absolute;top:0;display:flex;align-items:center;gap:8px;white-space:nowrap;}
  .contact-item svg{flex:none;}
  .brand-name{position:absolute;left:68px;top:90px;color:var(--white);font-weight:800;font-size:33px;letter-spacing:1px;line-height:1;}
  .headline{position:absolute;right:46px;top:94px;margin:0;color:var(--white);font-weight:800;font-size:30px;line-height:33px;text-align:right;}
  .service{position:absolute;height:21px;color:var(--white);font-weight:700;font-size:15.5px;line-height:21px;text-align:center;}
  .about-title{position:absolute;left:68px;top:668px;margin:0;color:var(--red);font-weight:700;font-size:19.5px;letter-spacing:.2px;}
  .about-body{position:absolute;left:68px;top:704px;width:379px;font-size:12.6px;line-height:14.6px;font-weight:500;color:#222;text-align:justify;}
  .about-body p{margin:0 0 14px;}
  .neighborhood-title{position:absolute;left:514px;top:738px;width:504px;margin:0;text-align:center;font-weight:700;font-size:18.5px;color:var(--charcoal);}
  .cta-text{position:absolute;left:330px;top:1118px;color:var(--white);font-weight:700;font-size:17.5px;}
  .cta-phone{position:absolute;left:668px;top:1104px;color:var(--white);font-weight:700;font-size:33px;letter-spacing:2.4px;}
</style>
</head>
<body>
<div class="flyer">
  <svg class="flyer-shapes" width="991" height="1200" viewBox="0 0 991 1200">
    <defs>
      <linearGradient id="hero-base" x1="0" y1="0" x2="0" y2="1">
        <stop offset="0" stop-color="var(--photo-sky)"/>
        <stop offset=".28" stop-color="#4a505a"/>
        <stop offset=".45" stop-color="var(--photo-siding)"/>
        <stop offset=".66" stop-color="#56606e"/>
        <stop offset=".76" stop-color="var(--photo-stone)"/>
        <stop offset=".84" stop-color="#3f4a2c"/>
        <stop offset=".9" stop-color="var(--photo-lawn)"/>
        <stop offset="1" stop-color="#74a04a"/>
      </linearGradient>
      <radialGradient id="hero-roof" cx=".45" cy=".33" r=".45">
        <stop offset="0" stop-color="var(--photo-roof)" stop-opacity=".75"/>
        <stop offset="1" stop-color="var(--photo-roof)" stop-opacity="0"/>
      </radialGradient>
      <radialGradient id="hero-light" cx=".45" cy=".5" r=".35">
        <stop offset="0" stop-color="#c9ccd2" stop-opacity=".45"/>
        <stop offset="1" stop-color="#c9ccd2" stop-opacity="0"/>
      </radialGradient>
      <radialGradient id="hero-right" cx=".95" cy=".6" r=".25">
        <stop offset="0" stop-color="#e8e6e0" stop-opacity=".6"/>
        <stop offset="1" stop-color="#e8e6e0" stop-opacity="0"/>
      </radialGradient>
      <linearGradient id="cottage-tone" x1="0" y1="0" x2="0" y2="1">
        <stop offset="0" stop-color="#8b95a8"/>
        <stop offset=".5" stop-color="#7a7f90"/>
        <stop offset=".75" stop-color="#c9a43a"/>
        <stop offset=".88" stop-color="#b4425a"/>
        <stop offset="1" stop-color="#4f8a36"/>
      </linearGradient>
      <linearGradient id="map-base" x1="0" y1="0" x2="1" y2="1">
        <stop offset="0" stop-color="#c3e3cb"/>
        <stop offset=".5" stop-color="var(--map-green)"/>
        <stop offset="1" stop-color="#a9d3b5"/>
      </linearGradient>
      <radialGradient id="map-town" cx=".42" cy=".5" r=".5">
        <stop offset="0" stop-color="#dfe6e3" stop-opacity=".9"/>
        <stop offset="1" stop-color="#dfe6e3" stop-opacity="0"/>
      </radialGradient>
    </defs>

    <g class="hero-photo" role="img" aria-label="Photo of a two-storey gray shingle-sided house with stone base, white trim and a green lawn">
      <rect x="0" y="48" width="991" height="560" fill="url(#hero-base)"/>
      <rect x="0" y="48" width="991" height="560" fill="url(#hero-roof)"/>
      <rect x="0" y="48" width="991" height="560" fill="url(#hero-light)"/>
      <rect x="0" y="48" width="991" height="560" fill="url(#hero-right)"/>
    </g>
    <polygon class="hero-cap" points="0,21 215,21 270,48 991,48 991,120 0,120" fill="var(--charcoal)"/>
    <polygon class="contact-strip" points="0,0 991,0 991,48 270,48 215,21 0,21" fill="var(--white)"/>
    <polygon class="headline-band" points="317,82 991,82 991,188 400,188" fill="var(--red)"/>

    <polygon class="page-white" points="0,597 991,500 991,1200 0,1200" fill="var(--white)"/>
    <polygon class="page-sand" points="365,597 991,500 991,1082 646,1082" fill="var(--sand)"/>

    <polygon points="582,590 991,590 991,611 602,611" fill="var(--red)"/>
    <polygon points="618,622 991,622 991,643 638,643" fill="var(--red)"/>
    <polygon points="685,654 991,654 991,675 705,675" fill="var(--red)"/>
    <polygon points="735,686 991,686 991,707 755,707" fill="var(--red)"/>

    <g class="area-map" role="img" aria-label="Road map of the west Georgia service area">
      <rect x="521" y="780" width="397" height="249" fill="url(#map-base)"/>
      <rect x="521" y="780" width="397" height="249" fill="url(#map-town)"/>
    </g>

    <polygon class="footer-corner" points="0,1000 140,1082 0,1082" fill="var(--charcoal)"/>
    <polygon class="footer-strip" points="298,1170 400,1170 440,1200 298,1200" fill="var(--charcoal)"/>
    <rect class="cta-band" x="280" y="1082" width="711" height="88" fill="var(--red)"/>
    <rect class="cottage-photo" x="0" y="1046" width="298" height="154" fill="url(#cottage-tone)" role="img" aria-label="Photo of a single-storey blue cottage with a colourful flower garden"/>
  </svg>

  <div class="contact-bar">
    <div class="contact-item" style="left:322px;">
      <svg width="14" height="22" viewBox="0 0 14 22"><rect x="1.5" y="1.5" width="11" height="19" rx="2.5" fill="none" stroke="var(--red)" stroke-width="2.4"/><rect x="4" y="5" width="6" height="7" fill="var(--red)"/></svg>
      <span>(555) 214-0387</span>
    </div>
    <div class="contact-item" style="left:510px;">
      <svg width="24" height="17" viewBox="0 0 24 17"><rect x="1.2" y="1.2" width="21.6" height="14.6" fill="none" stroke="var(--red)" stroke-width="2.2"/><polyline points="1.5,1.8 12,9.5 22.5,1.8" fill="none" stroke="var(--red)" stroke-width="2.2"/></svg>
      <span style="margin-left:10px;">hello@duomarkga.com</span>
    </div>
    <div class="contact-item" style="left:784px;">
      <svg width="14" height="20" viewBox="0 0 14 20"><path d="M7 0C3.1 0 0 3.1 0 7c0 5 7 13 7 13s7-8 7-13c0-3.9-3.1-7-7-7z" fill="var(--red)"/><circle cx="7" cy="7" r="2.6" fill="var(--white)"/></svg>
      <span style="margin-left:8px;">Halden, GA</span>
    </div>
  </div>

  <div class="brand-name">DUO MARK</div>

  <h1 class="headline">Services You Need with<br>The Quality You Deserve</h1>

  <div class="service" style="left:586px;top:590px;width:320px;">RESIDENTIAL ROOFING</div>
  <div class="service" style="left:628px;top:622px;width:320px;">COMMERCIAL ROOFING</div>
  <div class="service" style="left:716px;top:654px;width:200px;">SIDING</div>
  <div class="service" style="left:776px;top:686px;width:200px;">GUTTERS</div>

  <h2 class="about-title">GEORGIA’S EXPERTS AT ROOFING</h2>
  <div class="about-body">
    <p>Duo Mark is an industry leader in roofing repairs and installation. They have an experienced team of experts, with every member bringing their specialties to make sure you get a team of Georgia’s Best Roofers.</p>
    <p>Our company is known for its high level of expertise and excellent workmanship. We have a team of skilled professionals who can handle any job, large or small! Duo Mark also offers maintenance services if clients need them and installations, so give us a call today to learn more about what we offer. We ensure that each customer gets an experience like no other. Duo Mark is committed to customer satisfaction. We provide each client has their questions answered and all of the issues taken care of from start to finish. As a company, our top priority is always to satisfy the customers. We work hard so that they feel heard and understand your needs as an individual or business owner to give you what you want with quality no one else can offer. Our goal with each client is to have them leave happy, knowing that the best roofing company in their area took care of them and gave them a great deal on high-quality materials</p>
  </div>

  <h3 class="neighborhood-title">We're In Your Neighborhood!</h3>

  <div class="cta-text">Call Us for&nbsp; a free consultation</div>
  <div class="cta-phone">(555) 214-0387</div>
</div>
</body>
</html>
```